Alloy wheel repair business needs a website

Install logo previously purchased from pixelbazaar, toolbar with dropdowns. services, gallery, clients , contact ect
Maybe mission statment

Target Market(s)

vehicle owners, auto dealers,insurance companies,

Industry/Entity Type

Alloy Wheel Repair

Coding

Coded - Design and coding required

Number of Pages Required

4 page

Font styles to use
Sans Serif

Colors
0054AA
0677BA
7BADD7
CADEEF
E8F1F8

```html
<!DOCTYPE html>
<html lang="en">
<head>
<meta charset="utf-8">
<title>Spokeline Wheelworks</title>
<link rel="stylesheet" href="https://fonts.googleapis.com/css2?family=Figtree:wght@300;400;500;600;700;800&display=swap">
<style>
:root{
  --blue-deep:#0054AA;
  --blue:#0677BA;
  --blue-soft:#7BADD7;
  --blue-pale:#CADEEF;
  --blue-mist:#E8F1F8;
  --card-active:#E6EBF1;
  --icon-fill:#3a3d42;
  --ink:#1c1f24;
  --line:#e3e5e8;
  --white:#ffffff;
}
*{margin:0;padding:0;box-sizing:border-box}
html,body{width:1200px;height:859px;overflow:hidden;background:var(--white)}
body{font-family:"Figtree",sans-serif;color:var(--ink);position:relative}
.site-header{position:absolute;left:0;top:0;width:1200px;height:108px;background:var(--white);box-shadow:0 4px 10px rgba(0,0,0,.04);z-index:2}
.menu-close{position:absolute;left:36px;top:45px;width:20px;height:20px}
.header-divider{position:absolute;top:0;width:1px;height:108px;background:var(--line)}
.brand{position:absolute;left:112px;top:34px;display:flex;align-items:center;gap:10px}
.brand-mark{width:18px;height:18px;border-radius:50%;background:var(--blue)}
.brand-name{font-weight:800;font-size:22px;letter-spacing:.5px;color:var(--blue-deep);line-height:1.05}
.header-link{position:absolute;top:46px;display:flex;align-items:center;gap:6px;font-weight:600;font-size:14px;color:var(--ink)}
.search-icon{position:absolute;left:1141px;top:41px;width:26px;height:26px}
.side-nav{position:absolute;left:89px;top:166px;width:170px;list-style:none}
.side-nav li{height:36.3px;display:flex;align-items:center;justify-content:space-between;border-bottom:1px solid var(--line);font-size:13.4px;font-weight:500}
.side-nav li:last-child{border-bottom:none}
.side-nav li.is-current{color:var(--blue);font-weight:600}
.hero{position:absolute;left:294px;top:108px;width:816px;height:479px;background:radial-gradient(ellipse at 88% 80%,#a53d1a 0%,#5a2a1e 30%,transparent 60%),linear-gradient(100deg,#2a2a2c 0%,#4a4a4c 35%,#2b2626 60%,#3a2422 100%)}
.hero-photo{position:absolute;inset:0}
.hero-title{position:absolute;left:402px;top:168px;color:var(--white);line-height:1}
.hero-title strong{display:block;font-weight:700;font-size:38px;letter-spacing:-.3px}
.hero-title span{display:block;font-weight:300;font-size:45px;margin-top:2px;letter-spacing:-.3px}
.hero-sub{position:absolute;left:403px;top:256px;color:var(--white);font-size:11px}
.hero-btn{position:absolute;left:404px;top:284px;width:110px;height:30px;background:var(--blue);color:var(--white);font-size:12.5px;display:flex;align-items:center;justify-content:center}
.hero-next{position:absolute;left:790px;top:232px}
.hero-dots{position:absolute;left:268px;top:452px;display:flex;gap:16px;align-items:center}
.hero-dots i{width:5px;height:5px;border-radius:50%;background:var(--white)}
.hero-dots i.is-active{width:10px;height:10px;background:none;border:1.3px solid var(--white)}
.rule{position:absolute;left:0;top:586px;width:1200px;height:1px;background:var(--line)}
.services{position:absolute;left:90px;top:586px;display:flex;border:1px solid var(--line);border-top:none}
.service{width:204px;height:246px;border-left:1px solid var(--line);display:flex;flex-direction:column;align-items:center;padding-top:67px;text-align:center}
.service:first-child{border-left:none}
.service.is-active{background:var(--card-active)}
.service-icon{width:58px;height:58px;border-radius:50%;background:var(--icon-fill)}
.service h3{font-weight:400;font-size:13px;line-height:16.5px;margin-top:21px;text-transform:uppercase;color:var(--ink)}
.service .go{margin-top:9px}
</style>
</head>
<body>
<header class="site-header">
  <svg class="menu-close" viewBox="0 0 20 20"><path d="M1 1L19 19M19 1L1 19" stroke="#222" stroke-width="1.4"/></svg>
  <div class="header-divider" style="left:90px"></div>
  <div class="brand"><span class="brand-mark"></span><span class="brand-name">Spokeline<br>Wheelworks</span></div>
  <div class="header-link" style="left:853px">
    <svg width="12" height="17" viewBox="0 0 12 17"><path d="M6 1a5 5 0 0 0-5 5c0 4 5 10 5 10s5-6 5-10a5 5 0 0 0-5-5z" fill="none" stroke="var(--blue)" stroke-width="1.6"/><circle cx="6" cy="6" r="1.8" fill="var(--blue)"/></svg>
    Find a Location
  </div>
  <div class="header-link" style="left:992px">
    <svg width="11" height="16" viewBox="0 0 11 16"><path d="M3 1l2 0 1 4-2 1c.5 2.5 1.5 4 3 5l1.5-1.5 2.5 2.5-1.5 2.5C6 15 1 10 1 4z" fill="var(--blue)"/></svg>
    555 014 2288
  </div>
  <div class="header-divider" style="left:1110px"></div>
  <svg class="search-icon" viewBox="0 0 26 26"><circle cx="11.5" cy="11.5" r="10" fill="none" stroke="#222" stroke-width="1.8"/><path d="M19 19l6 6" stroke="#222" stroke-width="1.8"/></svg>
</header>

<ul class="side-nav">
  <li class="is-current">Home</li>
  <li>Services <svg width="12" height="7" viewBox="0 0 12 7"><path d="M1 1l5 5 5-5" fill="none" stroke="#333" stroke-width="1.2"/></svg></li>
  <li>Gallery</li>
  <li>Clients</li>
  <li>Find a Location <svg width="12" height="7" viewBox="0 0 12 7"><path d="M1 1l5 5 5-5" fill="none" stroke="#333" stroke-width="1.2"/></svg></li>
  <li>Contact Us</li>
</ul>

<section class="hero">
  <div class="hero-photo" role="img" aria-label="Close-up photograph of a multi-spoke alloy wheel on a car at sunset"></div>
  <h1 class="hero-title"><strong>Nationwide Wheel</strong><span>Repair &amp; Service</span></h1>
  <p class="hero-sub">High Quality Alloy Wheel Repair, OEM Replacements</p>
  <a class="hero-btn">Read More</a>
  <svg class="hero-next" width="10" height="18" viewBox="0 0 10 18"><path d="M1 1l8 8-8 8" fill="none" stroke="#fff" stroke-width="1.2"/></svg>
  <div class="hero-dots"><i class="is-active"></i><i></i><i></i><i></i></div>
</section>

<div class="rule"></div>

<section class="services">
  <article class="service">
    <div class="service-icon" role="img" aria-label="Wheel refinishing illustration"></div>
    <h3>Wheel<br>Refinishing</h3>
    <svg class="go" width="28" height="12" viewBox="0 0 28 12"><path d="M0 6h26M21 1l5 5-5 5" fill="none" stroke="#555" stroke-width="1.5"/></svg>
  </article>
  <article class="service is-active">
    <div class="service-icon" role="img" aria-label="Wheel straightening illustration"></div>
    <h3>Wheel<br>Straightening</h3>
    <svg class="go" width="28" height="12" viewBox="0 0 28 12"><path d="M0 6h26M21 1l5 5-5 5" fill="none" stroke="var(--blue)" stroke-width="1.8"/></svg>
  </article>
  <article class="service">
    <div class="service-icon" role="img" aria-label="Wheel remanufacturing illustration"></div>
    <h3>Wheel<br>Remanufacturing</h3>
    <svg class="go" width="28" height="12" viewBox="0 0 28 12"><path d="M0 6h26M21 1l5 5-5 5" fill="none" stroke="#555" stroke-width="1.5"/></svg>
  </article>
  <article class="service">
    <div class="service-icon" role="img" aria-label="Wheel custom coloring illustration"></div>
    <h3>Wheel<br>Custom Coloring</h3>
    <svg class="go" width="28" height="12" viewBox="0 0 28 12"><path d="M0 6h26M21 1l5 5-5 5" fill="none" stroke="#555" stroke-width="1.5"/></svg>
  </article>
  <article class="service">
    <div class="service-icon" role="img" aria-label="OEM wheel sales illustration"></div>
    <h3>OEM Wheel<br>Sales</h3>
    <svg class="go" width="28" height="12" viewBox="0 0 28 12"><path d="M0 6h26M21 1l5 5-5 5" fill="none" stroke="#555" stroke-width="1.5"/></svg>
  </article>
</section>
</body>
</html>
```